依頼詳細
駅前で配布するフライヤーの作成をお願いいたします。
韓流をイメージさせるようなポップなデザインを期待しております。
表面は店名のロゴメインでごちゃごちゃさせずに、裏面はリゾート感を押し出していただけたらと思っております。

記載項目
表面は店名のロゴのみ。
裏面は、以下の内容を記載してください。

Free drink ¥3,500 (Tax in ¥3,850円) / 1h

Cast drink ¥1,000 (Tax in ¥1,100) ~

Foods ¥700 (Tax in ¥770) ~

Address 兵庫県神戸市中央区若葉坂3丁目7-25 白樺テラスビル 4階
Phone 090-7264-3951

※上記金額にサービス料1名様10%、2名様以上5%を頂戴いたします。

上記住所より地図も作成してください。
サイズ
A6
ページ数
両面
希望イメージ
シンプル 複雑
単色 カラフル
暗い 明るい
日常 高級
遊び心 厳粛
未来的 伝統的
女性的 男性的
希望する色
赤系、黄・オレンジ系、韓国にあるような、蛍光管のポップな原色系
納品ファイル
• 高解像度JPG (.jpg)
• イラストレーター形式 (.ai)
補足説明
ネオンサイン例です。
ネオンサイン例です。
リアルな蛍光管のようなデザインが希望です。
Café&Barは業態の表示ですので、そこまで大きくせず、店名である『87』をもっと全面に押し出していただければ。

あと、裏面も表面と同じようなデザインでお願いします。
■ 選んだ理由

イメージとぴったりでした。

■ 提案者全員のお礼・コメント

今回は弊社コンペにご参加いただきありがとうございます。

魅力的な提案ばかりで選定に苦労いたしましたが、表面、裏面のイメージがピッタリな提案者の方にきめさせていただきました。

ありがとうございました。

```html
<!DOCTYPE html>
<html lang="ja">
<head>
<meta charset="utf-8">
<title>Price List</title>
<link href="https://fonts.googleapis.com/css2?family=Noto+Sans+JP:wght@400;500&display=swap" rel="stylesheet">
<style>
  :root {
    --bg-start: #b8f2d2;
    --bg-mid: #a9d8ea;
    --bg-end: #98aef4;
    --ink: #1a1a1a;
    --note: #1fa7c4;
    --map-light: #eef0f6;
    --map-mid: #c9cde0;
  }
  html, body {
    margin: 0;
    padding: 0;
    overflow: hidden;
  }
  .flyer {
    position: relative;
    width: 849px;
    height: 1200px;
    overflow: hidden;
    background: linear-gradient(100deg, var(--bg-start) 0%, var(--bg-mid) 50%, var(--bg-end) 100%);
    font-family: "Noto Sans JP", sans-serif;
    color: var(--ink);
  }
  .menu-item {
    position: absolute;
    left: 0;
    width: 100%;
    text-align: center;
  }
  .menu-item .name {
    margin: 0;
    font-size: 41px;
    font-weight: 400;
    line-height: 1;
  }
  .menu-item .price {
    margin: 22px 0 0;
    font-size: 38px;
    font-weight: 400;
    line-height: 1;
    white-space: nowrap;
  }
  .item-free { top: 116px; }
  .item-cast { top: 292px; }
  .item-foods { top: 468px; }
  .service-note {
    position: absolute;
    top: 662px;
    left: 0;
    width: 100%;
    margin: 0;
    text-align: center;
    color: var(--note);
    font-size: 27px;
    line-height: 42px;
  }
  .address {
    position: absolute;
    top: 780px;
    left: 0;
    width: 100%;
    text-align: center;
  }
  .address .label {
    margin: 0 0 12px;
    font-size: 29px;
    line-height: 1;
  }
  .address .lines {
    margin: 0;
    font-size: 28px;
    font-weight: 500;
    line-height: 43px;
    white-space: nowrap;
  }
  .map {
    position: absolute;
    left: 85px;
    top: 948px;
    width: 164px;
    height: 164px;
    background: linear-gradient(135deg, var(--map-light), var(--map-mid));
  }
  .phone {
    position: absolute;
    left: 360px;
    top: 994px;
    width: 300px;
    text-align: center;
    white-space: nowrap;
  }
  .phone .label {
    margin: 0 0 18px;
    font-size: 29px;
    line-height: 1;
  }
  .phone .number {
    margin: 0;
    font-size: 30px;
    line-height: 1;
  }
</style>
</head>
<body>
<div class="flyer">
  <section class="menu-item item-free">
    <h2 class="name">Free drink</h2>
    <p class="price">￥3,500 (Tax in ￥3,850円) / 1h</p>
  </section>
  <section class="menu-item item-cast">
    <h2 class="name">Cast drink</h2>
    <p class="price">￥1,000 (Tax in ￥1,100) ～</p>
  </section>
  <section class="menu-item item-foods">
    <h2 class="name">Foods</h2>
    <p class="price">￥700 (Tax in ￥770) ～</p>
  </section>

  <p class="service-note">※上記金額にサービス料1名様10%、<br>2名様以上5%を頂戴いたします。</p>

  <section class="address">
    <p class="label">Address</p>
    <p class="lines">兵庫県神戸市中央区若葉坂3丁目7-25<br>白樺テラスビル 4階</p>
  </section>

  <div class="map" role="img" aria-label="店舗周辺の地図"></div>

  <section class="phone">
    <p class="label">Phone</p>
    <p class="number">090-7264-3951</p>
  </section>
</div>
</body>
</html>
```